MOON FERN SIGNAGE

Signage size 750mm x 6000mm long full colour.
Background please see pixelbarn web site and see reference number 418 257 36
the text in the centre of the sign is to be in 3d bold script, to say
MOON FERN. Centre it and in slightly smaller text underneath write
PSYCHIC READINGS & HEALINGS
Then wherever best fits insert TEL: 8143 6097 and MOB: 0400 516 239

Keep the colours, heart and lines as similar as possible to the pixelbarn image, you could try and reflaect the heart logo on the left and rignt hand side (IDEAS?)

I then have to duplicate the above on another sign 750mm high x 3000mm wide (ALL the signs are landscape)
text says the same, and same font as before MOON FERN and underneath centred slightly smaller PSYCHIC READINGS & HEALINGS

Try different layouts, for example you could also try PSYCHIC READINGS on top of each other centred and to the left, then stack PSYCHIC READINGS
&
HEALINGS

Target Market(s)

Anyone who wants Psychic readings...NOT KID orientated...Audience probably 25 and onwards

Industry/Entity Type

Landscape

Requirements
Must have
• See pixelbarn heart and background as similar as you can

dimensions front sign 750mm x 6000mm

side sign 750mm x 3000mm

3d lettering, bold easy to read in contracsting colours to the background (See Pixelbarn 418 25736 image)

```html
<!DOCTYPE html>
<html lang="en">
<head>
<meta charset="utf-8">
<title>Moon Fern – Signage Artwork</title>
<link rel="stylesheet" href="https://fonts.googleapis.com/css2?family=Arimo:wght@400;700&family=Pacifico&display=swap">
<style>
  :root {
    --paper: #ffffff;
    --ink: #1a1a1a;
    --trim-mark: #b5b5b5;
    --magenta-hot: #d4157c;
    --magenta-deep: #8a0a4c;
    --plum-dark: #2a0216;
    --night: #050003;
    --glow: #ff6ec0;
    --type-light: #ffffff;
  }

  * { box-sizing: border-box; margin: 0; padding: 0; }

  html, body {
    width: 1200px;
    height: 216px;
    overflow: hidden;
    background: var(--paper);
  }

  .artboard {
    position: relative;
    width: 1200px;
    height: 216px;
    background: var(--paper);
    font-family: "Arimo", Arial, sans-serif;
  }

  .spec-note {
    position: absolute;
    left: 44px;
    top: 3px;
    font-size: 8px;
    line-height: 10px;
    color: var(--ink);
  }
  .spec-note dt { display: inline-block; width: 58px; }
  .spec-note dd { display: inline; }
  .spec-note dd::after { content: ""; display: block; }

  .trim-marks {
    position: absolute;
    inset: 0;
  }

  .sign-panel {
    position: absolute;
    left: 38px;
    top: 38px;
    width: 1124px;
    height: 140px;
    overflow: hidden;
    background:
      radial-gradient(ellipse 38% 120% at 50% 45%, var(--magenta-hot) 0%, var(--magenta-deep) 45%, var(--plum-dark) 78%, var(--night) 100%);
  }

  .light-sweep {
    position: absolute;
    top: 0;
    height: 140px;
    width: 260px;
  }
  .light-sweep--left {
    left: 0;
    background: radial-gradient(ellipse 90% 70% at 20% 75%, rgba(212, 21, 124, 0.35), rgba(0, 0, 0, 0) 70%);
  }
  .light-sweep--right {
    right: 0;
    background: radial-gradient(ellipse 90% 70% at 80% 55%, rgba(212, 21, 124, 0.35), rgba(0, 0, 0, 0) 70%);
  }

  .heart-emblem {
    position: absolute;
    left: 262px;
    top: 8px;
    width: 176px;
    height: 124px;
    border-radius: 50%;
    background: radial-gradient(ellipse at 50% 50%, rgba(255, 160, 215, 0.55), rgba(255, 110, 192, 0.2) 55%, rgba(255, 110, 192, 0) 75%);
  }

  .brand-name {
    position: absolute;
    left: 440px;
    top: -6px;
    width: 460px;
    font-family: "Pacifico", cursive;
    font-size: 74px;
    line-height: 120px;
    color: var(--type-light);
    text-shadow: 0 0 6px var(--glow), 0 0 14px var(--glow), 2px 3px 2px rgba(60, 0, 30, 0.7);
    white-space: nowrap;
  }

  .services {
    position: absolute;
    left: 489px;
    top: 109px;
    font-size: 20px;
    line-height: 24px;
    color: var(--type-light);
    white-space: nowrap;
  }

  .contact {
    position: absolute;
    right: 12px;
    top: 119px;
    font-size: 10.5px;
    font-weight: 700;
    line-height: 14px;
    color: var(--type-light);
    white-space: nowrap;
  }
</style>
</head>
<body>
<div class="artboard">

  <dl class="spec-note">
    <dt>Actual Size</dt><dd>: 6000mm x 750mm</dd>
    <dt>Artwork Size</dt><dd>: 600mm x 75mm</dd>
  </dl>

  <svg class="trim-marks" width="1200" height="216" viewBox="0 0 1200 216" aria-hidden="true">
    <g stroke="var(--trim-mark)" stroke-width="1">
      <line x1="38.5" y1="0" x2="38.5" y2="26"/>
      <line x1="1161.5" y1="0" x2="1161.5" y2="26"/>
      <line x1="38.5" y1="190" x2="38.5" y2="216"/>
      <line x1="1161.5" y1="190" x2="1161.5" y2="216"/>
      <line x1="0" y1="38.5" x2="26" y2="38.5"/>
      <line x1="0" y1="177.5" x2="26" y2="177.5"/>
      <line x1="1174" y1="38.5" x2="1200" y2="38.5"/>
      <line x1="1174" y1="177.5" x2="1200" y2="177.5"/>
    </g>
  </svg>

  <section class="sign-panel">
    <div class="light-sweep light-sweep--left" role="img" aria-label="Fine flowing pink light lines with sparkles"></div>
    <div class="light-sweep light-sweep--right" role="img" aria-label="Fine flowing pink light lines with sparkles"></div>

    <div class="heart-emblem" role="img" aria-label="Two glowing intertwined heart outlines"></div>

    <h1 class="brand-name">Moon Fern</h1>
    <p class="services">Psychic Readings &amp; Healings</p>
    <p class="contact">TEL: 8143 6097 and MOB: 0400 516 239</p>
  </section>

</div>
</body>
</html>
```